Penwick Mechanical Drain Cleaning and Jetting

We need to show our customers and potential customers that we now have the ability to perform Drain Cleaning, camera inspections, location services, and Hydro-Jetting Services. I would like the the colors to match the previous design.

```html
<!DOCTYPE html>
<html lang="en">
<head>
<meta charset="utf-8">
<title>Penwick Mechanical – Drain Cleaning and Jetting</title>
<link rel="stylesheet" href="https://fonts.googleapis.com/css2?family=Poppins:wght@400;500;600;700&family=Oswald:wght@600;700&display=swap">
<style>
  :root {
    --green: #13704a;
    --green-dark: #0e5a3b;
    --gold: #c9a640;
    --paper: #f2f2f1;
    --paper-shade: #e2e2e0;
    --ink: #2b2b2b;
    --stage: #dfe2e6;
    --white: #ffffff;
  }
  * { margin: 0; padding: 0; box-sizing: border-box; }
  html, body { width: 1200px; height: 800px; overflow: hidden; }
  body {
    background: var(--stage);
    font-family: "Poppins", sans-serif;
    position: relative;
  }
  .flyer {
    position: absolute;
    left: 338px; top: 30px;
    width: 524px; height: 740px;
    background: linear-gradient(160deg, var(--white), var(--paper) 55%, var(--paper-shade));
    overflow: hidden;
    box-shadow: 0 10px 30px rgba(0,0,0,.18);
  }
  .flyer-art { position: absolute; inset: 0; }
  .brand {
    position: absolute;
    left: 330px; top: 392px; width: 180px;
    color: var(--green);
    font-weight: 700;
    font-size: 22px;
    line-height: 1.02;
    letter-spacing: .5px;
    text-transform: uppercase;
    text-align: center;
  }
  .services {
    position: absolute;
    left: 300px; top: 458px; width: 210px;
    text-align: center;
  }
  .services-title {
    color: var(--green);
    font-family: "Oswald", sans-serif;
    font-weight: 600;
    font-size: 22px;
    letter-spacing: .5px;
    margin-bottom: 12px;
  }
  .service-list { list-style: none; }
  .service-item {
    display: flex; align-items: center; justify-content: center; gap: 8px;
    font-size: 14px; color: var(--ink);
    height: 34px;
  }
  .service-item svg { flex: none; }
  .headline-box {
    position: absolute;
    left: 10px; top: 502px;
    width: 300px; height: 140px;
    padding: 28px 0 0 28px;
    color: var(--white);
  }
  .headline-box .box-shape { position: absolute; inset: 0; z-index: 0; }
  .headline-box p { position: relative; z-index: 1; }
  .headline-lead { font-size: 19px; font-weight: 500; line-height: 1.1; }
  .headline-accent { font-size: 17px; font-weight: 500; color: var(--gold); line-height: 1.2; letter-spacing: .3px; }
  .headline-main { font-family: "Oswald", sans-serif; font-weight: 700; font-size: 30px; line-height: 1.15; letter-spacing: .3px; }
  .contact {
    position: absolute;
    left: 26px; top: 676px;
    font-size: 14px; color: var(--ink);
  }
  .contact-line { display: flex; align-items: center; gap: 12px; height: 26px; }
  .web-band {
    position: absolute;
    left: 268px; top: 676px;
    width: 256px; height: 46px;
    background: var(--green);
    border-radius: 12px 0 0 12px;
    display: flex; align-items: center; gap: 10px;
    padding-left: 20px;
    color: var(--white);
    font-size: 13px;
  }
</style>
</head>
<body>
<main class="flyer">
  <svg class="flyer-art" width="524" height="740" viewBox="0 0 524 740">
    <defs>
      <linearGradient id="photoTone" x1="0" y1="0" x2="1" y2="1">
        <stop offset="0" stop-color="#c9b08a"/>
        <stop offset=".35" stop-color="#e8e6e2"/>
        <stop offset=".7" stop-color="#9a9a98"/>
        <stop offset="1" stop-color="#d8d6d2"/>
      </linearGradient>
      <linearGradient id="jetTone" x1="0" y1="0" x2="1" y2="1">
        <stop offset="0" stop-color="#8e7f7a"/><stop offset="1" stop-color="#b6aaa3"/>
      </linearGradient>
      <linearGradient id="pinTone" x1="0" y1="0" x2="1" y2="1">
        <stop offset="0" stop-color="#efe6d8"/><stop offset="1" stop-color="#d9c9b4"/>
      </linearGradient>
      <linearGradient id="camTone" x1="0" y1="0" x2="1" y2="1">
        <stop offset="0" stop-color="#6d665e"/><stop offset="1" stop-color="#c7c4bf"/>
      </linearGradient>
    </defs>

    <path d="M0 0 H524 V196 C430 250 330 330 0 432 Z" fill="url(#photoTone)" role="img" aria-label="Photo of a plumber in overalls repairing the pipes under a kitchen sink"/>
    <path d="M0 446 C330 344 430 266 524 212" fill="none" stroke="var(--gold)" stroke-width="10"/>
    <path d="M0 470 C330 366 430 286 524 230" fill="none" stroke="var(--green)" stroke-width="14"/>

    <circle cx="444" cy="226" r="54" fill="url(#jetTone)" stroke="var(--green)" stroke-width="7" role="img" aria-label="Close-up of a hydro-jetting nozzle spraying water"/>
    <circle cx="298" cy="332" r="54" fill="url(#pinTone)" stroke="var(--green)" stroke-width="7" role="img" aria-label="Map with a red location pin"/>
    <circle cx="86" cy="410" r="58" fill="url(#camTone)" stroke="var(--green)" stroke-width="7" role="img" aria-label="Technician running a drain camera inspection reel"/>
  </svg>

  <div class="brand">Penwick<br>Mechanical</div>

  <section class="services">
    <h2 class="services-title">OUR SERVICES</h2>
    <ul class="service-list">
      <li class="service-item">Drain Cleaning <svg width="12" height="12" viewBox="0 0 12 12"><circle cx="6" cy="6" r="5" fill="none" stroke="var(--green)" stroke-width="1.4"/><path d="M3.5 6.2l1.7 1.6 3.3-3.4" fill="none" stroke="var(--green)" stroke-width="1.4"/></svg></li>
      <li class="service-item">Camera Inspection <svg width="12" height="12" viewBox="0 0 12 12"><circle cx="6" cy="6" r="5" fill="none" stroke="var(--green)" stroke-width="1.4"/><path d="M3.5 6.2l1.7 1.6 3.3-3.4" fill="none" stroke="var(--green)" stroke-width="1.4"/></svg></li>
      <li class="service-item">location services <svg width="12" height="12" viewBox="0 0 12 12"><circle cx="6" cy="6" r="5" fill="none" stroke="var(--green)" stroke-width="1.4"/><path d="M3.5 6.2l1.7 1.6 3.3-3.4" fill="none" stroke="var(--green)" stroke-width="1.4"/></svg></li>
      <li class="service-item">Hydro-Jetting <svg width="12" height="12" viewBox="0 0 12 12"><circle cx="6" cy="6" r="5" fill="none" stroke="var(--green)" stroke-width="1.4"/><path d="M3.5 6.2l1.7 1.6 3.3-3.4" fill="none" stroke="var(--green)" stroke-width="1.4"/></svg></li>
    </ul>
  </section>

  <div class="headline-box">
    <svg class="box-shape" width="300" height="140" viewBox="0 0 300 140">
      <path d="M0 24 Q0 0 24 0 H246 Q262 0 268 14 L298 118 Q302 140 280 140 H0 Z" fill="var(--green)"/>
    </svg>
    <p class="headline-lead">Have You</p>
    <p class="headline-accent">INSPECTED ALL YOUR</p>
    <p class="headline-main">PLUMING FIXTURES</p>
  </div>

  <div class="contact">
    <p class="contact-line"><svg width="12" height="12" viewBox="0 0 24 24"><path d="M6.6 10.8a15 15 0 006.6 6.6l2.2-2.2a1 1 0 011-.25 11.4 11.4 0 003.6.57 1 1 0 011 1V20a1 1 0 01-1 1A17 17 0 013 4a1 1 0 011-1h3.5a1 1 0 011 1c0 1.25.2 2.45.57 3.57a1 1 0 01-.25 1z" fill="var(--green)"/></svg>1-800.GO.PENWK</p>
    <p class="contact-line"><svg width="12" height="12" viewBox="0 0 24 24"><path d="M6.6 10.8a15 15 0 006.6 6.6l2.2-2.2a1 1 0 011-.25 11.4 11.4 0 003.6.57 1 1 0 011 1V20a1 1 0 01-1 1A17 17 0 013 4a1 1 0 011-1h3.5a1 1 0 011 1c0 1.25.2 2.45.57 3.57a1 1 0 01-.25 1z" fill="var(--green)"/></svg>555-014-2270</p>
  </div>

  <div class="web-band">
    <svg width="13" height="13" viewBox="0 0 24 24" fill="none" stroke="var(--white)" stroke-width="2"><circle cx="12" cy="12" r="10"/><path d="M2 12h20M12 2c3 3 3 17 0 20M12 2c-3 3-3 17 0 20"/></svg>
    www.penwickmechanical.com
  </div>
</main>
</body>
</html>
```